Hochzeits-Einladungen
Zielgruppe
Damen im Alter zwischen 25 - 40 Jahren, die gerade ihr Hochzeit planen
Aufgabenstellung
Gestaltung von Hochzeitskarten-Enladungen
Formate (in mm):
- geschlossen 145x145 (offen290x145)
ODER
- geschlossen 210x100 (offen420x100)
Vorgaben Design:
Es können auch Fotos des Paares als Design-Bestandteil eingebaut werden. Ein Foto oder mehrere (für diese Fotos einfach irgendwelche Paltzhalter verwenden – keine Fotos erwerben!)
Keine Verwendung von Sonderfarben (Digitaldruck ->CMYK) wie z.B. Gold, Silber etc..
Verwendung nur von Commercial-Use-Free-Fonts (Bitte hiervon auswählen: www.schriftkorbel.com)
Zur Abnahme:
Zuerst die Design-Entwürfe als PDF
Dann als InDesign (alles in unterschiedlichen Layern angelegt, die Illustrationen etc. als Vector und in CMYK)
klassisch - schlicht - mit hochzeitstypischen Illustrationen

```html
<!DOCTYPE html>
<html lang="de">
<head>
<meta charset="utf-8">
<title>Hochzeitseinladung – Lena &amp; Jonas</title>
<link rel="stylesheet" href="https://fonts.googleapis.com/css2?family=Poiret+One&display=swap">
<style>
  :root{
    --purple:#350893;
    --lavender:#8e7de0;
    --silver-dark:#a9aaae;
    --silver-mid:#d4d5d8;
    --silver-light:#f4f4f5;
    --text-grey:#6d6e72;
    --title-grey:#8b8c90;
    --fold:#b9b9bd;
    --page:#ffffff;
  }
  *{box-sizing:border-box;margin:0;padding:0}
  html,body{width:1200px;height:848px;overflow:hidden;background:var(--page)}
  body{position:relative;font-family:"Poiret One",sans-serif;color:var(--text-grey)}

  .spread{position:absolute;left:87px;width:1028px;background:var(--purple);
    box-shadow:2px 4px 6px rgba(0,0,0,.35);overflow:hidden}
  .spread--outside{top:140px;height:242px}
  .spread--inside{top:464px;height:243px}

  .band{position:absolute;left:0;width:100%;
    background:linear-gradient(180deg,var(--silver-mid) 0%,var(--silver-light) 35%,var(--silver-light) 55%,var(--silver-mid) 85%,var(--silver-dark) 100%);
    box-shadow:0 4px 4px rgba(0,0,0,.45)}
  .spread--outside .band{top:105px;height:76px}
  .spread--inside .band{top:80px;height:104px}

  .ornament{position:absolute;border-radius:38% 62% 42% 58% / 55% 40% 60% 45%;
    background:linear-gradient(150deg,rgba(142,125,224,.55) 0%,rgba(215,214,228,.45) 50%,rgba(142,125,224,.55) 100%)}

  .fold{position:absolute;left:600px;width:1px;background:var(--fold)}
  .fold--outside{top:122px;height:251px}
  .fold--inside{top:446px;height:250px}

  .address{position:absolute;left:246px;top:135px;width:180px;text-align:center;
    font-size:7.5px;line-height:14px;color:var(--text-grey)}
  .title{position:absolute;left:722px;top:112px;text-align:left;font-weight:400;color:var(--title-grey)}
  .title__word{display:block;font-size:27px;letter-spacing:.5px;line-height:30px}
  .title__names{display:block;font-size:22px;line-height:30px;color:#77787c}

  .details{position:absolute;left:702px;top:92px;width:160px;text-align:center;
    font-size:7px;line-height:12px;color:var(--text-grey)}
  .details p+p{margin-top:11px}

  .photo-card{position:absolute;left:228px;top:478px;width:210px;height:230px;
    transform:rotate(9deg);background:linear-gradient(180deg,#d9d9dc,#f2f2f3);
    border:1px solid #9a9a9e;box-shadow:2px 3px 6px rgba(0,0,0,.45);padding:8px}
  .photo-card__photo{width:100%;height:142px;
    background:linear-gradient(135deg,#2e2f33 0%,#8a8b8f 45%,#c9cacd 70%,#5b5c60 100%)}
  .photo-card__quote{margin-top:10px;text-align:center;font-size:8.5px;line-height:13px;color:#3a3b3f}
</style>
</head>
<body>

  <section class="spread spread--outside">
    <div class="band"></div>
    <div class="ornament" style="left:488px;top:7px;width:151px;height:216px" role="img" aria-label="Silbern-violettes florales Rankenornament"></div>
    <div class="ornament" style="left:845px;top:107px;width:183px;height:126px" role="img" aria-label="Silbern-violettes florales Rankenornament in der Ecke"></div>
    <p class="address">Unsere gemeinsame Adresse:<br>Musterstraße 1, 000 Musterhausen</p>
    <h1 class="title">
      <span class="title__word">EINLADUNG</span>
      <span class="title__names">Lena &amp; Jonas</span>
    </h1>
  </section>
  <div class="fold fold--outside"></div>

  <section class="spread spread--inside">
    <div class="band"></div>
    <div class="ornament" style="left:0;top:16px;width:166px;height:178px" role="img" aria-label="Silbern-violettes florales Rankenornament"></div>
    <div class="ornament" style="left:279px;top:70px;width:237px;height:172px" role="img" aria-label="Silbern-violettes florales Rankenornament"></div>
    <div class="ornament" style="left:512px;top:12px;width:141px;height:168px" role="img" aria-label="Silbern-violettes florales Rankenornament"></div>
    <div class="ornament" style="left:845px;top:70px;width:183px;height:173px" role="img" aria-label="Silbern-violettes florales Rankenornament in der Ecke"></div>
    <div class="details">
      <p>Unsere Trauung findet am<br>25. August 2012 um 13:30<br>am Standesamt Musterhausen statt.</p>
      <p>Zur Mitfeier und anschließenden<br>Hochzeitsfeier am laden wir herzlich ein.</p>
    </div>
  </section>
  <div class="fold fold--inside"></div>

  <figure class="photo-card">
    <div class="photo-card__photo" role="img" aria-label="Schwarzweißfoto der lachenden Braut im Schleier"></div>
    <figcaption class="photo-card__quote">Der Mensch allein ist<br>unvollkommen.<br>Er braucht einen zweiten,<br>um glücklich zu sein.</figcaption>
  </figure>

</body>
</html>
```